Salt Moon, Tin Heart

Hey Guys
Please visit our Chatterleaf page for the film. See what ideas you bring to the table for the movie poster.
Looking for creative and something fresh.
Check out cast on QVTK
Will use the stills from the film for actual poster and quality.
Thanks a million for taking an interest in our film. xoxo
Target Market(s)
2-50 year old, date night, girls night out
Industry/Entity Type
Movie

```html
<!DOCTYPE html>
<html lang="en">
<head>
<meta charset="utf-8">
<title>Salt Moon, Tin Heart — Poster</title>
<link rel="stylesheet" href="https://fonts.googleapis.com/css2?family=Anton&family=Open+Sans:wght@600&display=swap">
<style>
  :root {
    --sun: #fff200;
    --lagoon: #00ab9c;
    --lagoon-deep: #00897e;
    --ink-olive: #5c5200;
    --paper: #ffffff;
    --still-dark: #2c2b22;
    --still-mid: #55532f;
  }
  html, body {
    margin: 0;
    padding: 0;
    width: 710px;
    height: 1200px;
    overflow: hidden;
    background: var(--paper);
  }
  .poster {
    position: relative;
    width: 710px;
    height: 1200px;
    overflow: hidden;
    font-family: "Anton", "Impact", sans-serif;
  }
  .band-top {
    position: absolute;
    left: 0; top: 0;
    width: 710px; height: 400px;
    background: var(--sun);
  }
  .band-still {
    position: absolute;
    left: 0; top: 400px;
    width: 710px; height: 399px;
    display: block;
  }
  .band-bottom {
    position: absolute;
    left: 0; top: 799px;
    width: 710px; height: 401px;
    background: var(--lagoon);
  }
  .cast {
    position: absolute;
    top: 22px;
    left: 0;
    width: 710px;
    margin: 0;
    text-align: center;
    font-family: "Open Sans", sans-serif;
    font-weight: 600;
    font-size: 31px;
    color: var(--ink-olive);
    text-shadow: 0 0 3px #fffbb0;
    word-spacing: 4px;
  }
  .cast span + span { margin-left: 26px; }
  .title-line {
    position: absolute;
    margin: 0;
    font-size: 142px;
    line-height: 1;
    letter-spacing: 46px;
    text-transform: uppercase;
    white-space: nowrap;
  }
  .title-line--salt  { left: 24px;  top: 72px;  color: var(--lagoon); }
  .title-line--moon  { left: 24px;  top: 232px; color: var(--paper); text-shadow: 0 0 4px #f3e800; }
  .title-line--tin   { left: 150px; top: 787px; color: var(--sun);   text-shadow: 0 0 4px #7fe9dd; }
  .title-line--heart { left: 126px; top: 933px; color: var(--paper); text-shadow: 0 0 4px #7fe9dd; }
</style>
</head>
<body>
<main class="poster">
  <div class="band-top"></div>

  <svg class="band-still" viewBox="0 0 710 399" role="img" aria-label="Film still: a young man and young woman facing each other in close-up, overlaid with a cloud of romantic words">
    <defs>
      <linearGradient id="still-warm" x1="0" y1="0" x2="1" y2="0">
        <stop offset="0" stop-color="#4a4828"/>
        <stop offset="0.5" stop-color="var(--still-dark)"/>
        <stop offset="1" stop-color="#3a3a30"/>
      </linearGradient>
      <linearGradient id="still-cool" x1="0" y1="1" x2="1" y2="0">
        <stop offset="0" stop-color="#0f4f49"/>
        <stop offset="1" stop-color="#1f8f84"/>
      </linearGradient>
    </defs>
    <rect width="710" height="399" fill="url(#still-warm)"/>
    <polygon points="180,399 710,20 710,399" fill="url(#still-cool)"/>
  </svg>

  <div class="band-bottom"></div>

  <p class="cast"><span>Tessa Marlowe</span><span>Dane Corvin</span></p>

  <h1 class="title" aria-label="Salt Moon, Tin Heart">
    <span class="title-line title-line--salt">Salt</span>
    <span class="title-line title-line--moon">Moon</span>
    <span class="title-line title-line--tin">Tin</span>
    <span class="title-line title-line--heart">Heart</span>
  </h1>
</main>
</body>
</html>
```